Determining number of boxes of planks of flooring for a room

Need a creative design of an infographic of a room with instructions on how to measure the room and use this measurement to determine how much flooring to order.
The floor planks come in boxes and each box has 36 planks. Each box covers 5 metre squared in total.
The intent of the infographic is to help inform the customer how many boxes they need to order for their room.
The infographic should match the style of flooring being sold (image provided) and the logo for the company (image provided).
A crude sketch of instructions to measure a room and determine the number of boxes is provided in a document attached with this brief. Need improvement to the steps mentioned in this document on the infographic created.

```html
<!DOCTYPE html>
<html lang="en">
<head>
<meta charset="utf-8">
<title>Verdano – How many boxes to order</title>
<link rel="stylesheet" href="https://fonts.googleapis.com/css2?family=Montserrat:wght@400;600;700&family=Open+Sans:wght@400;600;700&display=swap">
<style>
  :root {
    --slate: #5a6a80;
    --slate-dark: #3f4d61;
    --slate-light: #c9d0da;
    --paper: #f3f4f6;
    --ink: #4a4f57;
    --ink-soft: #6d737c;
    --badge: #e07f45;
    --white: #ffffff;
  }
  * { box-sizing: border-box; margin: 0; padding: 0; }
  html, body { width: 849px; height: 1200px; overflow: hidden; background: var(--paper); }
  body { font-family: "Open Sans", Arial, sans-serif; color: var(--ink); }
  .canvas { position: relative; width: 849px; height: 1200px; overflow: hidden; background: var(--paper); }
  .abs { position: absolute; white-space: nowrap; }

  .brand { left: 40px; top: 34px; display: flex; align-items: center; gap: 14px; }
  .brand-mark { width: 44px; height: 44px; background: var(--slate); }
  .brand-name { font-family: "Montserrat", Arial, sans-serif; font-weight: 600; font-size: 44px; letter-spacing: 4px; color: var(--slate-dark); line-height: 1; }
  .brand-tagline { left: 100px; top: 90px; font-family: "Montserrat", Arial, sans-serif; font-size: 14px; letter-spacing: 3px; color: var(--ink-soft); }

  .hero-photo { position: absolute; right: 0; top: 0; width: 283px; height: 170px; background: linear-gradient(160deg, #e9e4dc 0%, #cfc3b2 55%, #a99079 100%); }

  .intro-title { left: 28px; top: 186px; font-family: "Montserrat", Arial, sans-serif; font-weight: 400; font-size: 25px; color: var(--slate); }
  .intro-text { position: absolute; left: 28px; top: 222px; width: 760px; font-size: 15.5px; line-height: 1.5; color: var(--ink-soft); }

  .section-band { position: absolute; left: 0; width: 849px; height: 56px; display: flex; align-items: center; color: var(--white); font-family: "Montserrat", Arial, sans-serif; font-weight: 700; font-size: 25px; white-space: nowrap; }
  .band-one { top: 396px; background: linear-gradient(90deg, var(--slate-light) 0%, var(--slate-light) 42%, var(--slate) 52%, var(--slate-dark) 100%); padding-left: 436px; }
  .band-two { top: 800px; background: linear-gradient(90deg, var(--slate-light) 0%, var(--slate) 30%, var(--slate-dark) 70%, var(--slate) 100%); padding-left: 320px; }

  .room-illustration { position: absolute; left: 28px; top: 467px; width: 397px; height: 303px; background: linear-gradient(150deg, #e7dccb 0%, #d3bfa2 50%, #9c8066 100%); }
  .box-illustration { position: absolute; left: 566px; top: 878px; width: 156px; height: 97px; background: linear-gradient(150deg, #ece6dc 0%, #d6c9b5 60%, #b8a58b 100%); }

  .step-title { font-family: "Montserrat", Arial, sans-serif; font-weight: 700; font-size: 16px; color: var(--ink); }
  .step-title .num { margin-right: 10px; color: var(--ink); }
  .step-sub { font-family: "Montserrat", Arial, sans-serif; font-weight: 700; font-size: 15px; color: var(--ink); }

  .badge { display: inline-flex; align-items: center; justify-content: center; width: 19px; height: 19px; border-radius: 50%; background: var(--badge); color: var(--white); font-size: 11px; font-weight: 700; flex: none; }
  .row { display: flex; align-items: center; gap: 8px; font-size: 11.5px; color: var(--ink-soft); }
  .formula { display: flex; align-items: center; gap: 9px; font-size: 18px; color: var(--ink); }
  .caption { font-size: 11.5px; color: var(--ink-soft); line-height: 1.35; white-space: nowrap; }
  .strong { font-weight: 700; color: var(--ink); }

  .note { position: absolute; left: 467px; top: 738px; width: 355px; font-size: 11.5px; line-height: 1.4; color: var(--ink-soft); }
  .note strong { color: var(--ink); }
</style>
</head>
<body>
<main class="canvas">
  <header>
    <div class="abs brand"><span class="brand-mark"></span><span class="brand-name">VERDANO</span></div>
    <div class="abs brand-tagline">PREMIUM FLOORS AND TILES</div>
    <div class="hero-photo" role="img" aria-label="Photo of a furnished room with vinyl plank flooring"></div>
    <h1 class="abs intro-title">How many boxes you have to order for your facility?</h1>
    <p class="intro-text">A long-lasting, waterproof vinyl flooring that's also easy to clean, will make a stunning addition to just about any space in your home. Kitchens, foyers, bathrooms.. the list goes on.<br>How much boxes of flooring you need to cover your facility???<br>Follow the 2 step below.</p>
  </header>

  <section>
    <h2 class="section-band band-one">1. Measure Room Dimensions</h2>
    <div class="room-illustration" role="img" aria-label="Illustration of a furnished room with length a and width b marked on the floor"></div>

    <div class="abs step-title" style="left:467px; top:485px;"><span class="num">1.1</span>Measure your installation location.</div>
    <div class="abs row" style="left:552px; top:518px;"><span class="badge">a</span>Length of Room (in Meter)</div>
    <div class="abs row" style="left:552px; top:544px;"><span class="badge">b</span>Length of Room (in Meter)</div>

    <div class="abs step-title" style="left:467px; top:586px;"><span class="num">1.2</span>Calculate Room Size</div>
    <div class="abs step-sub" style="left:502px; top:608px;">Multiply the room's length by its width.</div>
    <div class="abs formula" style="left:580px; top:640px;"><span class="badge">c</span>=<span class="badge">a</span>x<span class="badge">b</span></div>
    <div class="abs caption" style="left:566px; top:672px; text-align:center;">Room Size<br>(in Sq. Meter)</div>

    <p class="note"><strong>Note :</strong> If your room is not a square shape, please do a simple drawing and send it to us. We will be able to work it out for you.</p>
  </section>

  <section>
    <h2 class="section-band band-two">2. Work out Pack Numbers</h2>

    <div class="abs step-title" style="left:40px; top:874px;"><span class="num">2.1</span>Divide room size by 5</div>
    <div class="abs formula" style="left:110px; top:904px;"><span class="badge">d</span>=<span class="badge">c</span>/5</div>
    <div class="abs row" style="left:110px; top:946px;"><span class="badge">d</span><span class="strong">is Approximately Floor Pack</span></div>
    <div class="abs caption" style="left:137px; top:968px;">(Number of packs of floor<br>you need to cover this area.)</div>

    <div class="box-illustration" role="img" aria-label="Illustration of a box of flooring planks"></div>

    <div class="abs step-title" style="left:40px; top:1016px;"><span class="num">2.2</span>Round Up of Approximate Floor Pack</div>
    <div class="abs row" style="left:110px; top:1046px; align-items:flex-start;"><span>If</span><span class="badge">d</span><span style="white-space:normal; width:300px; line-height:1.35;">(Approximately Floor Pack) has decimal points, please always round up to the next integer</span></div>
    <div class="abs row" style="left:80px; top:1085px;">e.g. <span class="badge">d</span> is <u>3.1</u> - After Round Up it will be <u>4</u></div>
    <div class="abs row" style="left:111px; top:1117px;"><span class="badge">d</span> is <u>3.8</u> - After Round Up it will be <u>4</u></div>

    <div class="abs row" style="left:540px; top:1072px;"><span class="badge">e</span>= Round Up of <span class="badge">d</span></div>
    <div class="abs caption strong" style="left:520px; top:1102px; text-align:center;">Final Floor<br>Pack Numbers</div>
  </section>
</main>
</body>
</html>
```